Community Legal Website

The website is about a law in legal area (Fiscal), it has a moderator and the community also contributes with information.

Attention that this is not for a Law Firm. This is a community site where all the lawyers can contribute wiith their knowledge and at the same time where they can read the Official Law in the fiscal area.

The site is in portuguese, but we have attach information in english about the functionalities.

I attach information which represents the first version of the site done by html.. That is the site we intend to improve.

The site is quite simple because the main pages are:
- Home page;
- Section page (which has the Chapters and articles)
- Article page;

This pages all belong to the article:

redaccao_actual.htm, redaccoes_anteriores.htm, anotacoes.htm, jurisprudencia.htm, decisoesadministrativas.htm, minutas.htm, duvidas.htm

AS you see in all of them the options are always there.

The most important in this site is the usability of the content:

The FAQ, Contacts, Terms of conditions, who we are, are links less important.

Also there is a possibility to have in the homepage a higligh of certain articles that we want to raise from the others.

Please check the excel sheet as well as the zip file wich has the site in portuguese that you can use a website translator to check in your language.
Updates

We added a excel sheet with the functionalities in english which the site must have.

Reason: Because this is easter time we have increased the time for the deliver

Please check briefing update.

Reason: There were some request to extend the deadline because of the Easter

Hi!

Please read carefully the briefing. People are presenting me company web sites adn this is NOT a company web site. THis is a Site wich has a content of Laws. Please check the 1st version in the zip file and improve it. The options are there and you can translate in google tradutor or reading the excel sheet attach.

txs,
KM

Reason: My client need more desing choices

Target Market(s)

Lawyers, jurists and people related with the fiscal Law.

Industry/Entity Type

Legal

Requirements
Must have
• The interface should be clean and elegant.
It should also contribute to speed.
And try to avoid to many distract elements.
The site will be dinamic and with a backoffice, so in that you have to be carefully with the space dynamic. But you don't have to worry about the backoffice. Only the front office which is the public site.

```html
<!DOCTYPE html>
<html lang="pt">
<head>
<meta charset="utf-8">
<title>Código do IRS</title>
<link rel="stylesheet" href="https://fonts.googleapis.com/css2?family=Open+Sans:wght@300;400;600;700&display=swap">
<style>
  :root {
    --ink: #4a4a4a;
    --ink-soft: #7b7b7b;
    --slate: #5f7472;
    --teal: #5fa3ab;
    --rule: #e6e6e6;
    --footer: #b5b5b5;
    --footer-dot: #9c9c9c;
    --backdrop: #f6f6f6;
    --page: #ffffff;
  }
  * { box-sizing: border-box; margin: 0; padding: 0; }
  html, body { width: 1200px; height: 1064px; overflow: hidden; }
  body {
    position: relative;
    background: var(--page);
    font-family: "Open Sans", Arial, sans-serif;
    color: var(--ink);
  }
  .backdrop { position: absolute; inset: 0; z-index: 0; }
  .top-rule { position: absolute; left: 0; top: 0; width: 1200px; height: 7px; background: var(--slate); border-bottom: 2px solid #8fa9a7; z-index: 2; }

  .site-name {
    position: absolute; left: 216px; top: 120px; z-index: 2;
    display: flex; align-items: center; gap: 12px;
    font-size: 22px; font-weight: 300; color: #333; letter-spacing: 0.2px;
  }
  .site-name .mark { width: 18px; height: 18px; background: var(--slate); }

  .dotted-rule {
    position: absolute; height: 9px; z-index: 2;
    background-image: radial-gradient(circle, #c4c4c4 0.8px, transparent 1px);
    background-size: 3px 3px;
  }
  .dotted-rule.head { left: 171px; top: 189px; width: 843px; }
  .dotted-rule.foot { left: 396px; top: 979px; width: 618px; }

  .code-title {
    position: absolute; left: 171px; top: 248px; width: 843px; height: 40px; z-index: 2;
    background: var(--slate); color: #fff;
    font-size: 29px; font-weight: 300; letter-spacing: -1px;
    text-align: center; line-height: 40px;
  }

  .section { position: absolute; left: 396px; width: 618px; z-index: 2; }
  .section-label {
    height: 21px; background: var(--teal); color: #fff;
    font-size: 10px; letter-spacing: -0.5px; text-transform: uppercase;
    text-align: right; padding-right: 60px; line-height: 21px;
  }
  .articles { display: grid; grid-template-columns: 296px 292px; column-gap: 30px; list-style: none; }
  .articles li {
    height: 41px; line-height: 41px; border-bottom: 1px solid var(--rule);
    font-size: 15px; font-weight: 300; color: var(--ink-soft); letter-spacing: -0.4px;
    white-space: nowrap;
  }
  .articles li:nth-child(odd) { border-right: 1px solid #f0f0f0; }
  .articles li b { font-weight: 600; color: var(--ink); }

  .actions { position: absolute; top: 994px; left: 500px; z-index: 2; display: flex; gap: 0; }
  .action {
    position: absolute; display: flex; align-items: center; gap: 8px; white-space: nowrap;
    font-size: 13px; font-weight: 600; color: #3d3d3d; letter-spacing: -0.3px; top: 0;
  }
  .action svg { width: 18px; height: 18px; }

  .site-footer {
    position: absolute; left: 171px; top: 1021px; width: 843px; height: 41px; z-index: 2;
    background: var(--footer); color: #fff;
    display: flex; align-items: center; padding-left: 23px;
    font-size: 14px; font-weight: 300;
  }
  .site-footer .sep { margin: 0 10px; }
  .site-footer .contacts { position: absolute; left: 680px; font-size: 11px; letter-spacing: -0.5px; }
  .site-footer .social { position: absolute; left: 750px; display: flex; gap: 6px; }
  .site-footer .social span { width: 20px; height: 20px; border-radius: 50%; background: var(--footer-dot); }
</style>
</head>
<body>
  <svg class="backdrop" width="1200" height="1064" aria-hidden="true">
    <polygon points="0,0 1200,0 1200,12 0,952" fill="var(--backdrop)"/>
  </svg>
  <div class="top-rule"></div>

  <div class="site-name"><span class="mark"></span>CODEX FISCAL.net</div>
  <div class="dotted-rule head"></div>

  <h1 class="code-title">CÓDIGO DO IRS</h1>

  <section class="section" style="top:288px">
    <div class="section-label">Capítulo I - Incidência - Secção I - Incidência Real</div>
    <ul class="articles">
      <li><b>Artigo 1 .º -</b> Base do imposto</li>
      <li><b>Artigo 2 .º -</b> Rendimentos da categoria A</li>
      <li><b>Artigo 3 .º -</b> Rendimentos da categoria B</li>
      <li><b>Artigo 4.º -</b> Base do imposto</li>
      <li><b>Artigo 5 .º -</b> Base do imposto</li>
      <li><b>Artigo 6 .º -</b> Base do imposto</li>
      <li><b>Artigo 7 .º -</b> Base do imposto</li>
      <li><b>Artigo 8 .º -</b> Rendimentos da categoria A</li>
      <li><b>Artigo 9 .º -</b> Rendimentos da categoria B</li>
      <li><b>Artigo 10.º -</b> Base do imposto</li>
      <li><b>Artigo 11 .º -</b> Base do imposto</li>
      <li><b>Artigo 12.º -</b> Rendimentos da categoria A</li>
    </ul>
  </section>

  <section class="section" style="top:613px">
    <div class="section-label">Capítulo I - Incidência - Secção II - Incidência Pessoal</div>
    <ul class="articles">
      <li><b>Artigo 13 .º -</b> Rendimentos da categoria B</li>
      <li><b>Artigo 14.º -</b> Base do imposto</li>
      <li><b>Artigo 15 .º -</b> Base do imposto</li>
      <li><b>Artigo 16 .º -</b> Base do imposto</li>
      <li><b>Artigo 17 .º -</b> Base do imposto</li>
      <li><b>Artigo 18 .º -</b> Rendimentos da categoria A</li>
      <li><b>Artigo 19 .º -</b> Rendimentos da categoria B</li>
      <li><b>Artigo 20 .º -</b> Base do imposto</li>
    </ul>
  </section>

  <div class="dotted-rule foot"></div>

  <nav class="actions">
    <a class="action" style="left:10px">
      <svg viewBox="0 0 18 18"><circle cx="9" cy="10" r="7" fill="none" stroke="#3d3d3d" stroke-width="1.6"/><path d="M9 10 L12 7 M7 1.5 H11" stroke="#3d3d3d" stroke-width="1.6" fill="none"/></svg>
      Índice deste Código
    </a>
    <a class="action" style="left:178px">
      <svg viewBox="0 0 18 18"><path d="M9 2 V15 M5 15 H13 M2 5 H16 M4 5 L2 10 H6 Z M14 5 L12 10 H16 Z" stroke="#3d3d3d" stroke-width="1.3" fill="none"/></svg>
      Menu dos Códigos
    </a>
    <a class="action" style="left:335px">
      <svg viewBox="0 0 18 18"><path d="M3 13 L13 3 L15 5 L5 15 Z M1 16 H10" stroke="#3d3d3d" stroke-width="1.4" fill="none"/></svg>
      Gravar
    </a>
    <a class="action" style="left:437px">
      <svg viewBox="0 0 18 18"><rect x="3" y="1.5" width="12" height="15" fill="none" stroke="#3d3d3d" stroke-width="1.5"/><path d="M6 6 H12 M6 9 H12 M6 12 H12" stroke="#3d3d3d" stroke-width="1.3"/></svg>
      Imprimir
    </a>
  </nav>

  <footer class="site-footer">
    <span>Termos de utilização</span><span class="sep">|</span>
    <span>Perguntas frequentes</span><span class="sep">|</span>
    <span>Quem somos</span>
    <span class="contacts">CONTACTS</span>
    <div class="social"><span></span><span></span><span></span></div>
  </footer>
</body>
</html>
```